UI Improvement for FlorvaLink app

We are looking for a talented UI/UX designer to REFINE and enhance the visual design of our mobile application, FlorvaLink. The app is fully functional, but we need a designer to improve its aesthetics by specifying design elements such as fonts, colors, spacing, and component styles.
Your task will be to analyze the CURRENT UI and provide detailed design specifications that will make the app more visually appealing, modern, and user-friendly.
TODO:
Review the existing FlorvaLink app design (see attachments) and identify areas for visual improvement.
Provide a detailed UI style guide, including:
Typography (font choices, sizes, and weights)
Color palette (primary, secondary, and accent colors)
Component styling (buttons, forms, icons, and interactive elements)
Spacing and layout guidelines (margins, paddings, and alignment)
Ensure the design remains clean, modern, and professional while maintaining usability and accessibility.
Provide design mockups or visual examples (if possible) to illustrate the proposed changes.
Deliverables:
A UI Style Guide (PDF or Figma file) with specifications on fonts, colors, spacing, and UI components.
Optionally, before/after mockups or examples demonstrating the improvements.
Ideal Designer:
Strong experience in mobile UI/UX design.
Understanding of modern design trends and best practices.
Ability to communicate design choices clearly for easy developer implementation.
I have attached 7 images showcasing the main UI screens used in the FlorvaLink app. These screens need visual enhancements to improve their overall look and user experience.
The images represent the current design in three key modes:
LIST Mode – Displays data in a structured list format.
READ Mode – Shows detailed information when a user selects an item.
ADD/EDIT Mode – Allows users to input or modify information.
Additionally, there is a ‘MORE’ page, which serves as a menu listing other features of the application.
Task Objective:
Please refine and improve these UIs to create a more modern, visually appealing, and user-friendly experience. Focus on typography, colors, spacing, and component styling to ensure a cohesive and polished design.
Look and feel
Each slider illustrates characteristics of the customer's brand and the style your logo design should communicate.

```html
<!DOCTYPE html>
<html lang="en">
<head>
<meta charset="utf-8">
<title>FlorvaLink app – UI style guide</title>
<link href="https://fonts.googleapis.com/css2?family=Figtree:wght@400;500;600;700;800&family=Nunito+Sans:wght@400;600;700&family=Inter:wght@400;600;700&display=swap" rel="stylesheet">
<style>
:root{
  --primary:#1B7ECC;--ink:#1C1F34;--slate:#4B4B5A;--grey:#636669;--muted:#7C848B;
  --mist:#F2F6F7;--cloud:#E2E7F1;
  --cyan:#25C2E3;--green:#29BA85;--orange:#F77E53;--yellow:#FFBE0B;--pink:#FF5C75;--violet:#7859F4;
  --legacy-blue:#1a1ad6;--legacy-tag:#5ee35e;
}
*{margin:0;padding:0;box-sizing:border-box}
html,body{width:1200px;height:1129px;overflow:hidden;background:#fff}
body{position:relative;font-family:'Figtree',sans-serif;color:#000}
.abs{position:absolute}
.title{left:72px;top:72px;font-size:46px;font-weight:600;color:var(--slate);letter-spacing:0}
.section-label{font-size:17px;font-weight:600;color:var(--grey)}
.swatch{position:absolute;width:48px;height:48px;border-radius:4px;display:flex;align-items:center;justify-content:center;font-size:10.5px;color:#fff}
.swatch.light{color:#333}
.font-sample{font-size:39px;color:#000}
.band{left:72px;top:481px;width:1055px;height:44px;background:var(--primary);color:#fff;font-weight:700;font-size:17px;padding-left:12px;line-height:44px}

/* legacy screens */
.legacy{position:absolute;top:549px;width:234px;height:504px;background:#fff;overflow:hidden;font-family:'Inter',sans-serif}
.legacy .status{position:absolute;left:0;top:0;width:100%;height:29px;background:#000;color:#fff;font-size:10px;font-weight:600;padding:9px 0 0 34px}
.legacy .nav{position:absolute;left:0;top:29px;width:100%;height:36px;background:#e9eaee;text-align:center;font-size:10px;line-height:36px;color:#111}
.legacy .nav .act{position:absolute;top:0;font-size:14px;line-height:34px}
.legacy .list{position:absolute;left:0;top:65px;width:100%;height:396px;background:#e4e5e9;overflow:hidden}
.legacy .search{position:absolute;left:4px;top:68px;width:226px;height:21px;background:#fff;border:1px solid #9aa0aa;border-radius:3px;font-size:8.5px;color:#444;padding:4px 0 0 20px;z-index:2}
.legacy .search .adv{position:absolute;right:7px;top:2px;font-size:5.5px;line-height:7px;color:#9ab;text-align:center}
.card{position:absolute;left:5px;width:223px;height:48px;background:#f6f7f9;border-radius:2px;box-shadow:0 1px 1px rgba(0,0,0,.15)}
.card .letter{position:absolute;left:6px;top:5px;width:39px;height:39px;border:1px solid #4a5794;border-radius:2px;color:#888;font-size:14px;display:flex;align-items:center;justify-content:center}
.card .name{position:absolute;left:50px;top:9px;font-size:8.6px;font-weight:700;color:var(--legacy-blue);white-space:nowrap}
.card .tags{position:absolute;left:58px;top:31px;font-size:7.5px;font-weight:600;color:#111;white-space:nowrap}
.card .tags span{margin-right:8px}
.card .tags .q{background:var(--legacy-tag);padding:0 2px}
.legacy .tabs{position:absolute;left:0;top:461px;width:100%;height:43px;background:#fff}
.ltab{position:absolute;top:4px;width:48px;margin-left:-24px;text-align:center;font-size:6.3px;color:#111}
.ltab svg{display:block;margin:0 auto 4px}
.ltab.on{color:var(--primary)}
.home-bar{position:absolute;height:2px;border-radius:2px;background:#777}

/* refined screens */
.phone{position:absolute;top:540px;width:253px;height:525px;border:9px solid #0d0d0d;border-radius:38px;background:#fff;overflow:hidden;font-family:'Figtree',sans-serif}
.phone .time{position:absolute;left:22px;top:12px;font-size:10px;font-weight:700}
.phone .island{position:absolute;left:80px;top:7px;width:76px;height:22px;border-radius:11px;background:#0d0d0d}
.phone .sys{position:absolute;right:14px;top:14px}
.phone h1{position:absolute;left:10px;top:43px;font-size:17px;font-weight:700;color:var(--ink)}
.phone .add{position:absolute;left:183px;top:45px}
.phone .more{position:absolute;left:211px;top:51px}
.phone .search{position:absolute;left:10px;top:72px;width:214px;height:27px;border-radius:14px;background:var(--mist);font-size:10px;color:var(--muted);padding:7px 0 0 28px;font-family:'Nunito Sans',sans-serif}
.phone .search svg.mag{position:absolute;left:9px;top:7px}
.phone .search svg.filter{position:absolute;right:9px;top:7px}
.row{position:absolute;left:10px;width:220px;height:30px}
.avatar{position:absolute;left:0;top:0;width:30px;height:30px;border-radius:50%;color:#fff;font-size:8.5px;display:flex;align-items:center;justify-content:center;font-family:'Nunito Sans',sans-serif}
.row .name{position:absolute;left:40px;top:0;font-size:12px;color:var(--ink);white-space:nowrap}
.row .name.solo{top:8px}
.row .chips{position:absolute;left:40px;top:18px;display:flex;gap:3px}
.chip{font-family:'Nunito Sans',sans-serif;font-size:7px;color:var(--grey);background:var(--mist);border-radius:5px;padding:1px 5px}
.row .meta{position:absolute;left:40px;top:18px;font-family:'Nunito Sans',sans-serif;font-size:7.8px;color:var(--grey)}
.row .meta i{font-style:normal;color:#bbb;margin:0 3px}
.phone .tabs{position:absolute;left:0;top:456px;width:100%;height:60px;border-top:1px solid var(--cloud)}
.ntab{position:absolute;top:5px;width:46px;margin-left:-23px;text-align:center;font-size:5.8px;color:var(--muted)}
.ntab svg{display:block;margin:0 auto 3px}
.ntab.on{color:var(--primary)}
.phone .home-bar{height:3px;background:#0d0d0d;left:78px;top:501px;width:80px}
</style>
</head>
<body>

<div class="abs title">FlorvaLink app</div>

<div class="abs section-label" style="left:72px;top:201px">Colors</div>
<div class="swatch" style="left:72px;top:237px;background:var(--primary)">1B7ECC</div>
<div class="swatch" style="left:130px;top:237px;background:var(--ink)">1C1F34</div>
<div class="swatch" style="left:187px;top:237px;background:var(--slate)">4B4B5A</div>
<div class="swatch" style="left:245px;top:237px;background:var(--grey)">636669</div>
<div class="swatch" style="left:302px;top:237px;background:var(--muted)">7C848B</div>
<div class="swatch light" style="left:72px;top:299px;background:var(--mist)">F2F6F7</div>
<div class="swatch light" style="left:130px;top:299px;background:var(--cloud)">E2E7F1</div>
<div class="swatch" style="left:72px;top:362px;background:var(--cyan)">25C2E3</div>
<div class="swatch" style="left:130px;top:362px;background:var(--green)">29BA85</div>
<div class="swatch" style="left:187px;top:362px;background:var(--orange)">F77E53</div>
<div class="swatch" style="left:245px;top:362px;background:var(--yellow)">FFBE0B</div>
<div class="swatch" style="left:302px;top:362px;background:var(--pink)">FF5C75</div>
<div class="swatch" style="left:360px;top:362px;background:var(--violet)">7859F4</div>

<div class="abs section-label" style="left:480px;top:201px">Fonts</div>
<div class="abs font-sample" style="left:480px;top:236px;font-family:'Figtree',sans-serif">Figtree</div>
<div class="abs font-sample" style="left:480px;top:299px;font-family:'Nunito Sans',sans-serif">Nunito Sans</div>

<div class="abs band">List Page</div>

<!-- Legacy contacts -->
<div class="legacy" style="left:72px">
  <div class="status">3:01
    <svg class="abs" style="right:20px;top:9px" width="46" height="10" viewBox="0 0 46 10"><g fill="#fff"><circle cx="2" cy="7" r="1"/><circle cx="5" cy="7" r="1"/><circle cx="8" cy="7" r="1"/><circle cx="11" cy="7" r="1"/><path d="M16 3a8 8 0 0 1 10 0l-1.3 1.4a6 6 0 0 0-7.4 0zM18.5 5.6a4.5 4.5 0 0 1 5 0L21 8z"/><rect x="30" y="1.5" width="14" height="7" rx="2"/></g></svg>
  </div>
  <div class="nav">Contacts<span class="act" style="left:192px">+</span><span class="act" style="left:212px">···</span></div>
  <div class="list">
    <div class="card" style="top:29px"><div class="letter">A</div><div class="name">Ashford, Colin</div><div class="tags"><span>Aircraft Owner</span><span>Enthusiast -e</span><span>Flight Supp</span></div></div>
    <div class="card" style="top:79px"><div class="letter">A</div><div class="name">Archer, Dennis, Blake</div><div class="tags"><span>Aircraft Owner</span><span>Pilot</span><span class="q">Qualified Pilot</span></div></div>
    <div class="card" style="top:129px"><div class="letter">B</div><div class="name">Barrowman, Lionel</div><div class="tags"><span>Aircraft Owner</span><span>Pilot</span><span class="q">Qualified Pilot</span></div></div>
    <div class="card" style="top:179px"><div class="letter">B</div><div class="name">Brightwell, Owen</div><div class="tags"><span>Aircraft Owner</span><span>Pilot</span><span class="q">Qualified Pilot</span></div></div>
    <div class="card" style="top:229px"><div class="letter">C</div><div class="name">Corra, Elsa, Marie</div><div class="tags"><span>Pilot</span></div></div>
    <div class="card" style="top:279px"><div class="letter">C</div><div class="name">Castel Ruiz, Marco, Ileana</div><div class="tags"><span>Pilot</span></div></div>
    <div class="card" style="top:329px"><div class="letter">G</div><div class="name">Gaston, Reid</div><div class="tags"><span>Aircraft Owner</span><span>Pilot</span><span class="q">Qualified Pilot</span></div></div>
    <div class="card" style="top:379px"><div class="letter">G</div><div class="name">Gibbs, Nolan, Avery</div></div>
  </div>
  <div class="search">
    <svg class="abs" style="left:8px;top:5px" width="9" height="9" viewBox="0 0 10 10"><circle cx="4" cy="4" r="3.2" fill="none" stroke="#333" stroke-width="1"/><path d="M6.5 6.5 9 9" stroke="#333"/></svg>
    Search<div class="adv">Advanced<br>Search</div>
  </div>
  <div class="tabs">
    <div class="ltab on" style="left:23px"><svg width="8" height="8" viewBox="0 0 8 8"><circle cx="4" cy="2.2" r="2" fill="#1B7ECC"/><path d="M0 8a4 3 0 0 1 8 0z" fill="#1B7ECC"/></svg>Contact</div>
    <div class="ltab" style="left:70px"><svg width="8" height="8" viewBox="0 0 8 8"><rect x="1.5" y="0" width="5" height="2" fill="#111"/><circle cx="4" cy="3.6" r="1.6" fill="#111"/><path d="M0.5 8a3.5 2.6 0 0 1 7 0z" fill="#111"/></svg>Pilot</div>
    <div class="ltab" style="left:117px"><svg width="9" height="8" viewBox="0 0 9 8"><path d="M0 4 9 3.5V4.5L0 4ZM4 0h1l1.5 4L5 8H4l.5-4z" fill="#111"/></svg>Plane</div>
    <div class="ltab" style="left:164px"><svg width="8" height="8" viewBox="0 0 8 8"><path d="M3 0h1v4h3v3l-1 1H3L1 5l1-.5L3 5z" fill="#111"/></svg>Flt Request</div>
    <div class="ltab" style="left:211px"><svg width="8" height="8" viewBox="0 0 8 8"><circle cx="1.3" cy="4" r="0.9" fill="#111"/><circle cx="4" cy="4" r="0.9" fill="#111"/><circle cx="6.7" cy="4" r="0.9" fill="#111"/></svg>More</div>
  </div>
  <div class="home-bar" style="left:75px;top:499px;width:84px"></div>
</div>

<!-- Refined contact -->
<div class="phone" style="left:320px">
  <div class="time">9:41</div><div class="island"></div>
  <svg class="sys" width="48" height="8" viewBox="0 0 48 8"><g fill="#111"><rect x="0" y="5" width="2" height="3"/><rect x="3" y="3.5" width="2" height="4.5"/><rect x="6" y="2" width="2" height="6"/><rect x="9" y="0" width="2" height="8"/><path d="M16 3a7 7 0 0 1 9 0l-1.2 1.3a5 5 0 0 0-6.6 0zM18.3 5.4a4 4 0 0 1 4.4 0L20.5 8z"/><rect x="31" y="0.5" width="15" height="7" rx="2"/></g></svg>
  <h1>Contact</h1>
  <svg class="add" width="13" height="13" viewBox="0 0 13 13"><path d="M6.5 0v13M0 6.5h13" stroke="#1B7ECC" stroke-width="1.3"/></svg>
  <svg class="more" width="13" height="3" viewBox="0 0 13 3"><g fill="#1B7ECC"><circle cx="1.5" cy="1.5" r="1.2"/><circle cx="6.5" cy="1.5" r="1.2"/><circle cx="11.5" cy="1.5" r="1.2"/></g></svg>
  <div class="search">
    <svg class="mag" width="12" height="12" viewBox="0 0 12 12"><circle cx="5" cy="5" r="4" fill="none" stroke="#636669" stroke-width="1.1"/><path d="M8 8l3.5 3.5" stroke="#636669" stroke-width="1.1"/></svg>
    Search
    <svg class="filter" width="13" height="12" viewBox="0 0 13 12"><g fill="none" stroke="#636669" stroke-width="1"><path d="M0 3h7M10 3h3M0 9h3M6 9h7"/><circle cx="8.5" cy="3" r="1.5"/><circle cx="4.5" cy="9" r="1.5"/></g></svg>
  </div>

  <div class="row" style="top:118px"><div class="avatar" style="background:var(--green)">AC</div><div class="name">Ashford, Colin</div><div class="chips"><span class="chip">Aircraft Owner</span><span class="chip">Enthusiast</span><span class="chip">Flight Support</span></div></div>
  <div class="row" style="top:167px"><div class="avatar" style="background:var(--cyan)">ADB</div><div class="name">Archer, Dennis, Blake</div><div class="chips"><span class="chip">Aircraft Owner</span><span class="chip">Pilot</span><span class="chip">Qualified Pilot</span></div></div>
  <div class="row" style="top:217px"><div class="avatar" style="background:var(--yellow)">BO</div><div class="name">Brightwell, Owen</div><div class="chips"><span class="chip">Aircraft Owner</span><span class="chip">Pilot</span><span class="chip">Qualified Pilot</span></div></div>
  <div class="row" style="top:266px"><div class="avatar" style="background:var(--pink)">BL</div><div class="name">Barrowman, Lionel</div><div class="chips"><span class="chip">Aircraft Owner</span><span class="chip">Pilot</span><span class="chip">Qualified Pilot</span></div></div>
  <div class="row" style="top:315px"><div class="avatar" style="background:var(--orange)">CEM</div><div class="name">Corra, Elsa, Marie</div><div class="chips"><span class="chip">Pilot</span></div></div>
  <div class="row" style="top:365px"><div class="avatar" style="background:var(--violet)">CMI</div><div class="name">Castel Ruiz, Marco, Ileana</div><div class="chips"><span class="chip">Pilot</span></div></div>
  <div class="row" style="top:414px"><div class="avatar" style="background:var(--green)">GR</div><div class="name">Gaston, Reid</div><div class="chips"><span class="chip">Aircraft Owner</span><span class="chip">Pilot</span></div></div>

  <div class="tabs">
    <div class="ntab on" style="left:24px"><svg width="11" height="12" viewBox="0 0 11 12"><g fill="none" stroke="#1B7ECC" stroke-width="0.9"><rect x="1" y="0.5" width="9" height="11" rx="1.5"/><circle cx="5.5" cy="4.5" r="1.6"/><path d="M3 9a2.5 2 0 0 1 5 0"/></g></svg>Contact</div>
    <div class="ntab" style="left:71px"><svg width="11" height="12" viewBox="0 0 11 12"><g fill="none" stroke="#7C848B" stroke-width="0.9"><path d="M2.5 2.5h6L8 .5H3z"/><circle cx="5.5" cy="5" r="2"/><path d="M1 11.5a4.5 3.5 0 0 1 9 0z"/></g></svg>Pilot</div>
    <div class="ntab" style="left:118px"><svg width="12" height="12" viewBox="0 0 12 12"><path d="M6 .5c.8 0 1 1 1 2v2.5l4.5 2.5v1.2L7 7.5v2.3l1.5 1.2v.8L6 11l-2.5.8V11L5 9.8V7.5L.5 8.7V7.5L5 5V2.5c0-1 .2-2 1-2z" fill="none" stroke="#7C848B" stroke-width="0.8"/></svg>Plane</div>
    <div class="ntab" style="left:164px"><svg width="11" height="12" viewBox="0 0 11 12"><path d="M4 6V1.5a1 1 0 0 1 2 0V5l3.5.8a1 1 0 0 1 .8 1.1L9.7 11H4.5L1.8 8a1 1 0 0 1 1.4-1.3z" fill="none" stroke="#7C848B" stroke-width="0.8"/></svg>Flt Request</div>
    <div class="ntab" style="left:211px"><svg width="11" height="12" viewBox="0 0 11 12"><path d="M1 3h9M1 6h9M1 9h9" stroke="#7C848B" stroke-width="0.9"/></svg>More</div>
  </div>
  <div class="home-bar"></div>
</div>

<!-- Legacy pilots -->
<div class="legacy" style="left:636px">
  <div class="status">3:01
    <svg class="abs" style="right:20px;top:9px" width="46" height="10" viewBox="0 0 46 10"><g fill="#fff"><circle cx="2" cy="7" r="1"/><circle cx="5" cy="7" r="1"/><circle cx="8" cy="7" r="1"/><circle cx="11" cy="7" r="1"/><path d="M16 3a8 8 0 0 1 10 0l-1.3 1.4a6 6 0 0 0-7.4 0zM18.5 5.6a4.5 4.5 0 0 1 5 0L21 8z"/><rect x="30" y="1.5" width="14" height="7" rx="2"/></g></svg>
  </div>
  <div class="nav">Pilots<span class="act" style="left:192px">+</span><span class="act" style="left:212px">···</span></div>
  <div class="list">
    <div class="card" style="top:-13px"><div class="letter" style="top:5px"></div></div>
    <div class="card" style="top:41px"><div class="letter">A</div><div class="name">Archer, Dennis, Blake, 3182133, 9/30/24</div></div>
    <div class="card" style="top:91px"><div class="letter">B</div><div class="name">Barrowman, Lionel, 4467155, 2/28/25</div></div>
    <div class="card" style="top:141px"><div class="letter">B</div><div class="name">Brightwell, Owen, 2663187, 10/30/24, 16</div></div>
    <div class="card" style="top:191px"><div class="letter">C</div><div class="name">Corra, Elsa, Marie, 4360575, 3/30/25,</div></div>
    <div class="card" style="top:241px"><div class="letter">C</div><div class="name">Castel Ruiz, Marco, Ileana,</div></div>
    <div class="card" style="top:291px"><div class="letter">G</div><div class="name">Gaston, Reid, 3423819, 2/28/25,</div></div>
    <div class="card" style="top:341px"><div class="letter">G</div><div class="name">Gibbs, Nolan, Avery, 2761635, 3/6/23</div></div>
  </div>
  <div class="search">
    <svg class="abs" style="left:8px;top:5px" width="9" height="9" viewBox="0 0 10 10"><circle cx="4" cy="4" r="3.2" fill="none" stroke="#333" stroke-width="1"/><path d="M6.5 6.5 9 9" stroke="#333"/></svg>
    Search<div class="adv">Advanced<br>Search</div>
  </div>
  <div class="tabs">
    <div class="ltab" style="left:23px"><svg width="8" height="8" viewBox="0 0 8 8"><circle cx="4" cy="2.2" r="2" fill="#111"/><path d="M0 8a4 3 0 0 1 8 0z" fill="#111"/></svg>Contact</div>
    <div class="ltab on" style="left:70px"><svg width="8" height="8" viewBox="0 0 8 8"><rect x="1.5" y="0" width="5" height="2" fill="#1B7ECC"/><circle cx="4" cy="3.6" r="1.6" fill="#1B7ECC"/><path d="M0.5 8a3.5 2.6 0 0 1 7 0z" fill="#1B7ECC"/></svg>Pilot</div>
    <div class="ltab" style="left:117px"><svg width="9" height="8" viewBox="0 0 9 8"><path d="M0 4 9 3.5V4.5L0 4ZM4 0h1l1.5 4L5 8H4l.5-4z" fill="#111"/></svg>Plane</div>
    <div class="ltab" style="left:164px"><svg width="8" height="8" viewBox="0 0 8 8"><path d="M3 0h1v4h3v3l-1 1H3L1 5l1-.5L3 5z" fill="#111"/></svg>Flt Request</div>
    <div class="ltab" style="left:211px"><svg width="8" height="8" viewBox="0 0 8 8"><circle cx="1.3" cy="4" r="0.9" fill="#111"/><circle cx="4" cy="4" r="0.9" fill="#111"/><circle cx="6.7" cy="4" r="0.9" fill="#111"/></svg>More</div>
  </div>
  <div class="home-bar" style="left:75px;top:499px;width:84px"></div>
</div>

<!-- Refined pilot -->
<div class="phone" style="left:884px">
  <div class="time">9:41</div><div class="island"></div>
  <svg class="sys" width="48" height="8" viewBox="0 0 48 8"><g fill="#111"><rect x="0" y="5" width="2" height="3"/><rect x="3" y="3.5" width="2" height="4.5"/><rect x="6" y="2" width="2" height="6"/><rect x="9" y="0" width="2" height="8"/><path d="M16 3a7 7 0 0 1 9 0l-1.2 1.3a5 5 0 0 0-6.6 0zM18.3 5.4a4 4 0 0 1 4.4 0L20.5 8z"/><rect x="31" y="0.5" width="15" height="7" rx="2"/></g></svg>
  <h1>Pilot</h1>
  <svg class="add" width="13" height="13" viewBox="0 0 13 13"><path d="M6.5 0v13M0 6.5h13" stroke="#1B7ECC" stroke-width="1.3"/></svg>
  <svg class="more" width="13" height="3" viewBox="0 0 13 3"><g fill="#1B7ECC"><circle cx="1.5" cy="1.5" r="1.2"/><circle cx="6.5" cy="1.5" r="1.2"/><circle cx="11.5" cy="1.5" r="1.2"/></g></svg>
  <div class="search">
    <svg class="mag" width="12" height="12" viewBox="0 0 12 12"><circle cx="5" cy="5" r="4" fill="none" stroke="#636669" stroke-width="1.1"/><path d="M8 8l3.5 3.5" stroke="#636669" stroke-width="1.1"/></svg>
    Search
    <svg class="filter" width="13" height="12" viewBox="0 0 13 12"><g fill="none" stroke="#636669" stroke-width="1"><path d="M0 3h7M10 3h3M0 9h3M6 9h7"/><circle cx="8.5" cy="3" r="1.5"/><circle cx="4.5" cy="9" r="1.5"/></g></svg>
  </div>

  <div class="row" style="top:118px"><div class="avatar" style="background:var(--cyan)">ADB</div><div class="name">Archer, Dennis, Blake</div><div class="meta">3182133<i>•</i>9/30/24</div></div>
  <div class="row" style="top:167px"><div class="avatar" style="background:var(--yellow)">BO</div><div class="name">Brightwell, Owen</div><div class="meta">2663187<i>•</i>10/30/24</div></div>
  <div class="row" style="top:217px"><div class="avatar" style="background:var(--pink)">BL</div><div class="name">Barrowman, Lionel</div><div class="meta">4467155<i>•</i>2/28/25</div></div>
  <div class="row" style="top:266px"><div class="avatar" style="background:var(--orange)">CEM</div><div class="name">Corra, Elsa, Marie</div><div class="meta">4360575<i>•</i>3/30/25</div></div>
  <div class="row" style="top:315px"><div class="avatar" style="background:var(--violet)">CMI</div><div class="name solo">Castel Ruiz, Marco, Ileana</div></div>
  <div class="row" style="top:365px"><div class="avatar" style="background:var(--green)">GR</div><div class="name">Gaston, Reid</div><div class="meta">3423819<i>•</i>2/28/23</div></div>
  <div class="row" style="top:414px"><div class="avatar" style="background:var(--cyan)">GNA</div><div class="name">Gibbs, Nolan, Avery</div><div class="meta">2761635<i>•</i>3/6/23G</div></div>

  <div class="tabs">
    <div class="ntab" style="left:24px"><svg width="11" height="12" viewBox="0 0 11 12"><g fill="none" stroke="#7C848B" stroke-width="0.9"><rect x="1" y="0.5" width="9" height="11" rx="1.5"/><circle cx="5.5" cy="4.5" r="1.6"/><path d="M3 9a2.5 2 0 0 1 5 0"/></g></svg>Contact</div>
    <div class="ntab on" style="left:71px"><svg width="11" height="12" viewBox="0 0 11 12"><g fill="none" stroke="#1B7ECC" stroke-width="0.9"><path d="M2.5 2.5h6L8 .5H3z"/><circle cx="5.5" cy="5" r="2"/><path d="M1 11.5a4.5 3.5 0 0 1 9 0z"/></g></svg>Pilot</div>
    <div class="ntab" style="left:118px"><svg width="12" height="12" viewBox="0 0 12 12"><path d="M6 .5c.8 0 1 1 1 2v2.5l4.5 2.5v1.2L7 7.5v2.3l1.5 1.2v.8L6 11l-2.5.8V11L5 9.8V7.5L.5 8.7V7.5L5 5V2.5c0-1 .2-2 1-2z" fill="none" stroke="#7C848B" stroke-width="0.8"/></svg>Plane</div>
    <div class="ntab" style="left:164px"><svg width="11" height="12" viewBox="0 0 11 12"><path d="M4 6V1.5a1 1 0 0 1 2 0V5l3.5.8a1 1 0 0 1 .8 1.1L9.7 11H4.5L1.8 8a1 1 0 0 1 1.4-1.3z" fill="none" stroke="#7C848B" stroke-width="0.8"/></svg>Flt Request</div>
    <div class="ntab" style="left:211px"><svg width="11" height="12" viewBox="0 0 11 12"><path d="M1 3h9M1 6h9M1 9h9" stroke="#7C848B" stroke-width="0.9"/></svg>More</div>
  </div>
  <div class="home-bar"></div>
</div>

</body>
</html>
```